Flyer Design

Hi, This work has potential to expand! After the flyers I could be looking to improve my website design and our van needs brandingPlease find attached what I would like (or if you can improve the design) on the front of my flyer. I will also provide pictures for the back. I am not sure how I want this laid out. (i have attached a picture called idea, I like this for some reason but might not work for me) My husband is young (32) and we have built a website (www.kelvomark.co.uk) but we haven't gone fully live yet as he is still working for someone elseAnyway, I want to set him apart from all the rest. I want vibrant colors which is eye catchy and interesting. Makes people want to read it and not put the flyer in the binThe reason these pictures are more about conservatories, patios (smaller building work) is becasue these first lot of flyers are aimed at a new build site with 1000 homes per site. They will only be looking for conservatoies, driveways, small alterations. Maybe the conservatory could be in the middle? Again, I don't know please stick to the logo which is on the bottom left of my design but the rest is up to you. I also had a little play with the brick in the logo to maybe make it a background design somewhere. Might be rubbish ideaI did not get any help with the website so if the Flyers take the branding/colours in a different direction/theme there could be work to go forward with continuous improvement on the website AND we want to brand the vanI look forward to seeing your deignThank you for your help!Maelle
Updates
Project Deadline Extended Reason: Thank you for your efforts so far. My husband and I are reviewing the flyers and it's harder to chose the design that we like than we thought. I hope to improve the brief and interact with you more as I think we know have a better understanding of what we are looking forI will improve the brief in the next 24 hoursKind regardsSaoirse Added Saturday, January 31, 2015
Industry/Entity Type
Building
Look and feel
Each slider illustrates characteristics of the customer's brand and the style your logo design should communicate.

```html
<!DOCTYPE html>
<html lang="en">
<head>
<meta charset="utf-8">
<title>Kelvomark Building Services Flyer</title>
<link href="https://fonts.googleapis.com/css2?family=Questrial&family=Roboto:wght@500;700&family=Open+Sans:wght@600;700&display=swap" rel="stylesheet">
<style>
  :root{
    --stage:#262626;
    --navy:#1d3a5f;
    --navy-text:#34476a;
    --green:#9bc53d;
    --panel:#eef1f4;
    --white:#ffffff;
    --grey:#444;
  }
  *{box-sizing:border-box;margin:0;padding:0}
  html,body{width:1200px;height:1200px;overflow:hidden;background:var(--stage)}
  .canvas{position:relative;width:1200px;height:1200px}
  .card{position:absolute;background:var(--white);overflow:hidden}

  /* back side */
  .back{left:412px;top:38px;width:752px;height:528px}
  .back .ph{position:absolute}
  .ph-house{left:7px;top:7px;width:246px;height:184px;background:linear-gradient(160deg,#d9d4cc 0%,#a46a4e 45%,#6f8f4a 100%)}
  .ph-bricks{left:7px;top:198px;width:246px;height:186px;background:linear-gradient(180deg,#f4f8ea,#e4efc9)}
  .ph-flowers{left:7px;top:358px;width:247px;height:164px;background:linear-gradient(135deg,#d66aa8 0%,#f2f2f2 35%,#7aa04a 70%,#9a8a70 100%)}
  .ph-patio{left:263px;top:358px;width:237px;height:164px;background:linear-gradient(160deg,#e7ece5 0%,#6c8a5a 50%,#8c8478 100%)}
  .ph-deck{left:510px;top:358px;width:236px;height:164px;background:linear-gradient(180deg,#b7c8a4 0%,#8a6f55 45%,#a08a72 100%)}
  .about{position:absolute;left:268px;top:7px;width:478px;height:344px;background:linear-gradient(180deg,#f3f5f7,#e6eaee);padding:12px 16px;font-family:"Questrial",sans-serif;font-size:13.4px;line-height:1.32;color:var(--navy-text)}
  .about p{margin-bottom:7px}

  /* front side */
  .front{left:36px;top:624px;width:751px;height:528px}
  .ph-wall{position:absolute;left:0;top:0;width:751px;height:366px;background:linear-gradient(180deg,#dfe6e4 0%,#b6674a 25%,#a9553a 60%,#5e7d45 88%,#47683a 100%)}
  .services{position:absolute;left:13px;top:70px;list-style:none;font-family:"Roboto",sans-serif;font-weight:500;font-size:19.5px;letter-spacing:.3px;color:var(--white)}
  .services li{height:25.8px;line-height:25.8px}
  .services span{background:var(--navy);padding:0 5px 0 4px;display:inline-block}
  .band{position:absolute;left:0;top:366px;width:751px;height:24px;background:var(--green)}
  .footer{position:absolute;left:0;top:390px;width:751px;height:138px;background:linear-gradient(180deg,#fbfbfb,#ececec)}
  .brand{position:absolute;left:18px;top:424px;font-family:"Open Sans",sans-serif;color:var(--navy)}
  .brand-row{display:flex;align-items:center;gap:8px}
  .brand-mark{width:22px;height:22px;background:var(--green)}
  .brand-name{font-weight:700;font-size:40px;line-height:1;letter-spacing:-.5px}
  .brand-tag{font-weight:600;font-size:22px;margin-top:4px}
  .ph-person{position:absolute;left:410px;top:372px;width:142px;height:156px;background:linear-gradient(180deg,#c9a88f 0%,#efefef 55%,#e2e2e2 100%)}
  .contact{position:absolute;left:560px;top:402px;width:180px;font-family:"Questrial",sans-serif;color:var(--grey)}
  .contact h2{font-weight:400;font-size:22px;line-height:28px;color:var(--green);border-bottom:1px solid #999;padding-bottom:2px;white-space:nowrap}
  .contact h2 b{font-family:"Roboto",sans-serif;font-weight:700;color:var(--navy)}
  .contact ul{list-style:none;margin-top:4px}
  .contact li{display:flex;align-items:center;gap:7px;font-size:15px;height:21.5px;white-space:nowrap}
  .contact svg{width:12px;height:12px;flex:none;fill:var(--green)}
</style>
</head>
<body>
<main class="canvas">

  <section class="card back">
    <div class="ph ph-house" role="img" aria-label="Photo of a brick conservatory with white window frames and a garden"></div>
    <div class="ph ph-bricks" role="img" aria-label="Decorative pattern of repeated green bricks"></div>
    <div class="about">
      <p>We have many years of experience in the building trade. From new builds and renovations to extensions and loft/garage conversions. No job to big or too small.</p>
      <p>We are one of the lucky few that actually enjoy our jobs. That's what serves us best in putting the extra care and attention into our customers' homes.</p>
      <p>We provide a value-added construction service to our customers by creating a successful partnership. Our pledge is to establish lasting relationships with our customers by exceeding their expectations through exceptional professionalism and quality of work by all of our construction team.</p>
      <p>We want kelvomark to be more than just our company name to you. We give our customers a personal professional service and work on each project as if it was our own home.</p>
      <p>It would be an honor to bring your grand designs to life and meeting our team and seeing our work will definitely fill you with confidence.</p>
    </div>
    <div class="ph ph-flowers" role="img" aria-label="Photo of a curved stone flower bed with pink and white flowers beside a lawn"></div>
    <div class="ph ph-patio" role="img" aria-label="Photo of a paved garden patio with table, chairs and parasol"></div>
    <div class="ph ph-deck" role="img" aria-label="Photo of a timber deck with wooden railings and garden chairs"></div>
  </section>

  <section class="card front">
    <div class="ph-wall" role="img" aria-label="Photo of a red brick garden wall with white pillar caps, a round window opening and shrubs"></div>
    <ul class="services">
      <li><span>BRICK WALLS</span></li>
      <li><span>PATIOS &amp; DECKING</span></li>
      <li><span>FENCING</span></li>
      <li><span>CONSERVATORIES</span></li>
      <li><span>DRIVEWAYS</span></li>
      <li><span>GARAGE CONVERTIONS</span></li>
      <li><span>EXTENSIONS</span></li>
      <li><span>FASCIAS &amp; SOFFITS</span></li>
      <li><span>GUTTERING</span></li>
      <li><span>PROPERY ALTERATIONS</span></li>
    </ul>
    <div class="band"></div>
    <div class="footer"></div>
    <div class="brand">
      <div class="brand-row"><span class="brand-mark"></span><span class="brand-name">kelvomark</span></div>
      <div class="brand-tag">Building Services</div>
    </div>
    <div class="ph-person" role="img" aria-label="Photo of the builder in a white shirt with arms folded"></div>
    <div class="contact">
      <h2>Contact <b>ROWAN</b></h2>
      <ul>
        <li><svg viewBox="0 0 16 16"><path d="M3 1l3 3-2 2c1 2 3 4 5 5l2-2 3 3-2 3C6 15 1 10 0 4z"/></svg>01632 960417</li>
        <li><svg viewBox="0 0 16 16"><path d="M4 0h8v16H4zM5.5 2v9h5V2zM7 12.5h2v2H7z" fill-rule="evenodd"/></svg>07700 900318</li>
        <li><svg viewBox="0 0 16 16"><path d="M0 3h16v10H0zM1 4l7 5 7-5"/></svg>info@kelvomark.co.uk</li>
        <li><svg viewBox="0 0 16 16"><circle cx="8" cy="8" r="7.5"/></svg>www.kelvomark.co.uk</li>
      </ul>
    </div>
  </section>

</main>
</body>
</html>
```